Guided Study Tour - Klangtage Dornhalm Two Sided Flyer

We need a two-sided flyer for a Guided Study Tour to Klangtage Dornhalm. We want beautiful pictures of Germany and if possible some of the Velter venues our participants will be visiting. I have also provided the content that needs to be included. Also, in the attached document I provided a link to the Klangtage event. Please read and watch the video to be inspired.
This flyer should be beautiful and engaging. It needs to grab your attention right away and really highlight the wonderful things that they will be doing and that are included in the tour. This is a once in a lifetime opportunity for people to experience. We are targeting Music Directors and Music professionals.
Both attached logos need to be present on the flyer.

```html
<!DOCTYPE html>
<html lang="en">
<head>
<meta charset="utf-8">
<title>Guided Study Tour – Klangtage Dornhalm Flyer</title>
<link href="https://fonts.googleapis.com/css2?family=Montserrat:wght@700&family=Mulish:wght@400;600&family=Kaushan+Script&family=Libre+Baskerville:ital@1&display=swap" rel="stylesheet">
<style>
  :root{
    --bg:#ece9e4;
    --paper:#f1f1f3;
    --navy:#1f2a5c;
    --red:#c4202e;
    --maroon:#8a0f1c;
    --orange:#f07a1a;
    --amber:#f6a43c;
    --sun:#f5cf6e;
    --gold:#f4c863;
    --ink:#2c2c2c;
    --purple:#5a3f8e;
  }
  *{box-sizing:border-box;margin:0;padding:0}
  html,body{width:1200px;height:1200px;overflow:hidden;background:var(--bg)}
  body{position:relative;font-family:"Mulish",Arial,sans-serif;color:var(--ink)}
  .page{position:absolute;top:150px;width:546px;height:770px;background:var(--paper);overflow:hidden;box-shadow:0 4px 12px rgba(0,0,0,.18)}
  .page--front{left:30px}
  .page--back{left:624px;background:var(--sun)}
  .abs{position:absolute}

  /* front */
  .top-band{left:0;top:0;width:546px;height:52px;background:linear-gradient(90deg,#4a2b6a,#8e2640 50%,#6e1f3c)}
  .top-stripe{left:0;top:52px;width:546px;height:5px;background:var(--amber)}
  .hero{left:0;top:57px;width:546px;height:334px;background:linear-gradient(90deg,#e9d3df 0%,#c9a7b8 45%,#8f7480 70%,#6c5a62 100%)}
  .statue{left:330px;top:86px;width:216px;height:305px;background:linear-gradient(180deg,#4a3d37,#2a221e 70%,#3a2f2a);border-radius:90px 90px 0 0;opacity:.9}
  .script{font-family:"Kaushan Script",cursive;color:var(--navy)}
  .title-small{left:50px;top:100px;font-size:30px}
  .title-big{left:24px;top:150px;font-size:62px;color:var(--gold);-webkit-text-stroke:2px var(--navy);transform:rotate(-6deg);transform-origin:left center}
  .subtitle{left:28px;top:254px;width:296px;font-size:12.5px;line-height:17px}
  .date{left:68px;top:314px;font-size:10.5px;font-weight:600;color:var(--navy)}
  .bar-navy{left:0;top:391px;width:273px;height:9px;background:var(--navy)}
  .bar-orange{left:273px;top:391px;width:273px;height:9px;background:var(--amber)}
  .heading{font-family:"Montserrat",Arial,sans-serif;font-weight:700;color:var(--red);font-size:18px}
  .col-left{left:18px;top:416px;width:250px}
  .col-right{left:292px;top:416px;width:250px}
  .divider{left:273px;top:418px;width:2px;height:204px;background:var(--red)}
  .checks{list-style:none;margin-top:9px;font-size:10.3px;line-height:16.5px}
  .checks li{position:relative;padding-left:14px}
  .checks li .ind{display:block;padding-left:9px}
  .checks li::before{content:"";position:absolute;left:1px;top:5px;width:7px;height:4px;border-left:2px solid #333;border-bottom:2px solid #333;transform:rotate(-45deg)}
  .performers{left:32px;top:576px;width:236px;font-size:9.6px;line-height:13px}
  .performers b{display:block;font-family:"Montserrat",Arial,sans-serif;color:var(--red);font-size:10.5px;margin-bottom:1px}
  .swoosh{left:0;width:546px}
  .quote{left:100px;top:726px;width:346px;text-align:center;font-family:"Libre Baskerville",Georgia,serif;font-style:italic;font-size:7.4px;line-height:12.5px;color:var(--maroon)}
  .quote small{display:block;font-size:6px}

  /* back */
  .city{left:0;top:0;width:546px;height:360px}
  .intro{left:290px;top:70px;width:254px;padding:6px 8px;background:rgba(20,22,50,.55);color:#fff;font-size:9.6px;line-height:12.8px}
  .plane{left:22px;top:298px}
  .trip-title{left:24px;top:340px;font-size:16px}
  .inc-left{left:22px;top:366px;width:260px}
  .inc-right{left:282px;top:366px;width:256px}
  .back .checks{font-size:9.6px;line-height:14.6px;margin-top:0}
  .portrait-slot{left:56px;top:664px;font-size:9px}
  .bio{left:190px;top:611px;width:340px;font-size:8.2px;line-height:10.9px}
  .footer{left:0;top:711px;width:546px;height:59px;background:linear-gradient(90deg,var(--purple),#8c2b5a 45%,var(--red))}
  .brand{color:#fff;font-family:"Mulish",Arial,sans-serif;font-weight:600;font-size:14px;display:flex;align-items:center;gap:7px}
  .brand i{display:block;width:20px;height:20px;border-radius:50%;background:#fff}
  .brand-left{left:22px;top:730px}
  .brand-right{left:388px;top:730px}
  .email-notch{left:190px;top:711px}
  .email{left:190px;top:717px;width:200px;text-align:center;font-size:9px;color:var(--red);font-weight:600}
</style>
</head>
<body>

<section class="page page--front">
  <div class="abs top-band" role="img" aria-label="Stained glass church windows"></div>
  <div class="abs top-stripe"></div>
  <div class="abs hero" role="img" aria-label="Stone church facade in soft evening light"></div>
  <div class="abs statue" role="img" aria-label="Bronze statue of the composer Velter in front of the church"></div>

  <div class="abs script title-small">Guided Study Tour</div>
  <div class="abs script title-big">Klangtage</div>
  <p class="abs script subtitle">Plus day trips to Wittenberg and Weimar, and guided tours in Berlin, Dresden, &amp; two nights in Prague!</p>
  <p class="abs date">June 12-16, 2019 | Dornhalm, Germany</p>

  <div class="abs bar-navy"></div>
  <div class="abs bar-orange"></div>

  <div class="abs col-left">
    <h2 class="heading" style="padding-left:14px">Klangtage Highlights:</h2>
    <ul class="checks">
      <li>More than 100 Concerts in 42 different<span class="ind">Velter venues</span></li>
      <li>World Class Musicians &amp; Celebrated<span class="ind">Recording Artists</span></li>
      <li>Day trips to Weimer &amp; Dresden</li>
      <li>Bilingual pre-concert talks &amp; lectures with<span class="ind">Velter Scholars</span></li>
    </ul>
  </div>
  <div class="abs divider"></div>
  <div class="abs col-right">
    <h2 class="heading" style="padding-left:14px">Study Tour Highlights:</h2>
    <ul class="checks">
      <li>Access to dress rehearsals</li>
      <li>Meet the artist opportunities</li>
      <li>Post-concert discussions led by Adrian Holt</li>
      <li>Study sessions on Velter's B-Minor Mass,<span class="ind">Magnificat, St. John Passion,</span><span class="ind">St. Matthew Passion &amp; Weimar</span><span class="ind">Cantatashours</span></li>
      <li>Guidance in planning individual<span class="ind">concert itinerary</span></li>
      <li>Professional development or continuing<span class="ind">education credit</span></li>
    </ul>
  </div>
  <p class="abs performers"><b>Featured Performers:</b>Marco Velasquez, Henk Laarman, Vocalis Nova, Dornhalm Hall Orchestra, Lunaria, &amp; the Dornhalm Boys Choir</p>

  <svg class="abs swoosh" style="top:620px" width="546" height="150" viewBox="0 0 546 150">
    <path d="M0 80 C120 10 330 -10 546 70 L546 100 C360 40 150 40 0 110 Z" fill="var(--maroon)"/>
    <path d="M0 110 C150 50 360 40 546 100 L546 112 C360 60 160 70 0 128 Z" fill="var(--amber)"/>
    <path d="M0 128 C160 70 360 62 546 112 L546 126 C360 80 170 90 0 150 Z" fill="var(--orange)"/>
  </svg>
  <p class="abs quote">“This is where it all has begun...this is why our guests have tears in their eyes listening to the St. Matthew Passion or the B-Minor Mass”<small>~ Lukas Brenner, Musicologist, Festival Director</small></p>
</section>

<section class="page page--back back">
  <svg class="abs city" width="546" height="360" viewBox="0 0 546 360" role="img" aria-label="Cathedral and river bridge at dusk with city lights">
    <defs>
      <linearGradient id="dusk" x1="0" y1="0" x2="0" y2="1">
        <stop offset="0" stop-color="#3d4a7a"/>
        <stop offset=".35" stop-color="#c9846a"/>
        <stop offset=".6" stop-color="#3a3152"/>
        <stop offset="1" stop-color="#b86a2a"/>
      </linearGradient>
    </defs>
    <path d="M0 0 H546 V250 C420 350 230 360 0 270 Z" fill="url(#dusk)"/>
    <path d="M0 270 C230 360 420 350 546 250 V278 C420 380 220 380 0 290 Z" fill="var(--maroon)"/>
    <path d="M546 250 C470 320 360 345 240 350 C380 360 480 320 546 278 Z" fill="var(--red)"/>
  </svg>
  <p class="abs intro">After many years of attending Klangtage, Dr. Adrian Holt has partnered with Meridian Crest to create a memorable study tour centered around the 2019 festival. Meridian Crest Tours, powered by Halden Tours, is utilizing their more than 100 years of combined travel expertise to design a custom tour for all who love the music of the Baroque era.</p>

  <svg class="abs plane" width="60" height="38" viewBox="0 0 60 38" aria-hidden="true">
    <path d="M2 22 L46 12 C54 10 58 12 56 16 C54 19 50 20 46 21 L30 25 L18 37 L12 37 L20 27 L8 30 L4 34 L0 34 L3 27 Z M24 16 L14 4 L20 4 L34 13 Z" fill="var(--red)"/>
  </svg>
  <h2 class="abs heading trip-title">TRIP INCLUSIONS</h2>
  <ul class="abs checks inc-left">
    <li>Roundtrip Airfare from Houston</li>
    <li>13 Nights Accomodations,<span class="ind">3 Star Hotels with A/C</span></li>
    <li>Daily Breakfast</li>
    <li>Access to rehearsal sessions</li>
    <li>Pirvate Luxury Coach Transfer Services<span class="ind">for airport transfers and day tours to Berlin,</span><span class="ind">Weimar and Dresden &amp; Prague.</span></li>
    <li>Professional Local Guides for City Tours in:<span class="ind">Berlin, Weimar, Dresden &amp; Prague</span></li>
  </ul>
  <ul class="abs checks inc-right">
    <li>Entrance fees to: Ferenc Adler-Haus, House of<span class="ind">Jonas Reiter, National Museum &amp; House of</span><span class="ind">Emmerich Falk in Weimer, Lutherian Frauenkirche,</span><span class="ind">Gallery of Old Masters – Zwinger, Castle of</span><span class="ind">Prague, St. George's Basilica, Old Place,</span><span class="ind">Golden Lane, and the St. Vitus Cathedral.</span></li>
    <li>All Applicable Taxes and Gratuities<span class="ind">for Included Services, Guides, and Drivers</span></li>
    <li>$2 Million in Professional Liability Insurance</li>
    <li>24-hour Travel Support Staff</li>
  </ul>

  <svg class="abs swoosh" style="top:530px" width="546" height="240" viewBox="0 0 546 240">
    <path d="M0 70 C150 0 400 -10 546 40 V240 H0 Z" fill="var(--red)"/>
    <path d="M0 84 C160 20 400 14 546 56 V240 H0 Z" fill="var(--amber)"/>
    <path d="M0 98 C170 40 400 34 546 76 V240 H0 Z" fill="var(--paper)"/>
  </svg>
  <p class="abs portrait-slot">Adrian's image</p>
  <p class="abs bio">Adrian Holt is Director of Choral Studies at the Rio Verde State University and the conductor of the Verde Symphony Chorale and the Verde Choral Artists, a professional chamber choir. A native Texan, his degrees are from Crestmoor University, Linwood College and Pacific Coast University. Recent engagements include conducting the Morlaix Requiem in Buffalo, NY, serving on the jury for the Aegean International Choral Festival in Preveza, Greece and the International Choir Championship Cantus Nova in Tusnia, Bosnia and Herzogevina.</p>

  <div class="abs footer"></div>
  <svg class="abs email-notch" width="200" height="26" viewBox="0 0 200 26" aria-hidden="true">
    <path d="M0 0 C30 0 40 24 100 24 C160 24 170 0 200 0 Z" fill="var(--paper)"/>
  </svg>
  <p class="abs email">a.holt@rioverde.edu</p>
  <div class="abs brand brand-left"><i></i>Halden Tours</div>
  <div class="abs brand brand-right"><i></i>Meridian Crest</div>
</section>

</body>
</html>
```